Quellbyte Business cards template

We're looking for something modern and elegant. We are a reseller of technology (computers, datacenter, etc). Color theme would be "only" white with the incorporation of the blue that's present on our website (Quellbyte.com) and logo file. We would like for the card to provide all the necessary info for the specific person (Phone#, fax#, email, name, website URL) . I'm attaching the logo file to this request. Please have it show Montreal/New York somewhere, without providing specific addresses.

Target Market(s)

All b2b

Industry/Entity Type

Business

Contact Information for Business Card

Please have the color scheme be represented by only the white and blue from our website (Quellbyte.com) and logo. We would like to logo on the card, but not big and overwhelming. This card will be used as a template for anybody within the company, it should display the user's name, phone#, fax#, email, job title and website URL. Please have it show Montreal/New York somewhere, without providing our specific addresses. Really, we're looking for a clean, simple and elegant look.

Font styles to use
Serif

Requirements
Must have
• Please see card details
Nice to have
• Please see card details
Should not have
• Anything tacky or tagline.

```html
<!DOCTYPE html>
<html lang="en">
<head>
<meta charset="utf-8">
<title>Quellbyte Business Cards</title>
<link rel="stylesheet" href="https://fonts.googleapis.com/css2?family=Lora:wght@400;600;700&display=swap">
<style>
  :root {
    --stage: #222222;
    --blue-top: #0491d9;
    --blue-bottom: #0271ba;
    --blue-deep: #0470bc;
    --blue-bright: #0a8fd6;
    --blue-name: #0a6ab8;
    --white: #ffffff;
    --ink: #1a1a1a;
  }
  * { box-sizing: border-box; margin: 0; padding: 0; }
  html, body {
    width: 1189px;
    height: 1200px;
    overflow: hidden;
    background: var(--stage);
    font-family: "Lora", Georgia, serif;
  }
  .stage { position: relative; width: 1189px; height: 1200px; }
  .card {
    position: absolute;
    left: 171px;
    width: 856px;
    height: 488px;
    overflow: hidden;
    box-shadow: 2px 3px 6px rgba(0,0,0,0.6);
  }
  .card--front {
    top: 67px;
    background: linear-gradient(to bottom, var(--blue-top), var(--blue-bottom));
  }
  .card--back { top: 626px; background: var(--blue-deep); }
  .front-wordmark {
    position: absolute;
    left: 0; right: 0;
    top: 190px;
    text-align: center;
    color: var(--white);
    font-size: 82px;
    font-weight: 600;
    letter-spacing: 1px;
    line-height: 1;
  }
  .back-shape { position: absolute; inset: 0; }
  .back-wordmark {
    position: absolute;
    left: 41px;
    top: 118px;
    color: var(--blue-bright);
    font-size: 70px;
    font-weight: 600;
    line-height: 1;
  }
  .person { position: absolute; left: 41px; top: 262px; }
  .person__name {
    color: var(--blue-name);
    font-size: 30px;
    font-weight: 400;
    line-height: 1.05;
  }
  .person__title { color: var(--ink); font-size: 23px; line-height: 1.1; }
  .contact { position: absolute; left: 41px; top: 360px; list-style: none; }
  .contact__item {
    display: flex;
    align-items: center;
    height: 32px;
    font-size: 23px;
    color: var(--ink);
  }
  .contact__icon {
    width: 24px; height: 24px;
    margin-right: 9px;
    flex: none;
  }
  .website {
    position: absolute;
    left: 398px;
    top: 424px;
    font-size: 23px;
    color: var(--ink);
  }
  .website__domain { color: var(--blue-bright); }
</style>
</head>
<body>
<main class="stage">
  <section class="card card--front" aria-label="Card front">
    <div class="front-wordmark">Quellbyte</div>
  </section>

  <section class="card card--back" aria-label="Card back">
    <svg class="back-shape" width="856" height="488" viewBox="0 0 856 488" aria-hidden="true">
      <path d="M0,88 C150,34 280,18 380,19 C610,22 812,140 812,300 C812,385 755,440 669,488 L0,488 Z" fill="var(--white)"/>
      <path d="M673,107 C780,170 830,240 823,310 C816,390 760,442 684,488" fill="none" stroke="var(--blue-bright)" stroke-width="5"/>
    </svg>

    <div class="back-wordmark">Quellbyte</div>

    <div class="person">
      <h1 class="person__name">NOAH PELLETIER</h1>
      <p class="person__title">Managing Partner</p>
    </div>

    <ul class="contact">
      <li class="contact__item">
        <svg class="contact__icon" viewBox="0 0 24 24" aria-label="Phone">
          <rect width="24" height="24" fill="var(--blue-bright)"/>
          <path d="M4,10 Q12,4 20,10 L18,12 L15,10 L9,10 L6,12 Z" fill="var(--white)"/>
          <rect x="7" y="12" width="10" height="7" rx="1" fill="var(--white)"/>
        </svg>
        (01) 2345 6789
      </li>
      <li class="contact__item">
        <svg class="contact__icon" viewBox="0 0 24 24" aria-label="Fax">
          <rect width="24" height="24" fill="var(--blue-bright)"/>
          <rect x="8" y="4" width="8" height="6" fill="var(--white)"/>
          <rect x="4" y="10" width="16" height="7" rx="1" fill="var(--white)"/>
          <rect x="7" y="15" width="10" height="5" fill="var(--white)" stroke="var(--blue-bright)" stroke-width="1"/>
        </svg>
        (01) 2345 6789
      </li>
      <li class="contact__item">
        <svg class="contact__icon" viewBox="0 0 24 24" aria-label="Email">
          <rect width="24" height="24" fill="var(--blue-bright)"/>
          <rect x="4" y="6" width="16" height="12" fill="none" stroke="var(--white)" stroke-width="1.6"/>
          <path d="M4,6 L12,13 L20,6 M4,18 L10,12 M20,18 L14,12" fill="none" stroke="var(--white)" stroke-width="1.4"/>
        </svg>
        Info@yourcompany.com
      </li>
    </ul>

    <p class="website">www.<span class="website__domain">yourcompany</span>.com</p>
  </section>
</main>
</body>
</html>
```